Packaging for a Kids' Drink Mix

Brightly Our Finest produces a powdered drink mix for children call Moonrocket Meals for Kids, An organic drink mix which provides 100% of the recommended daily allowance of fruits, veggies and protein. The label must attract an American audience. We would like to use kids' colors, fonts and ideas. It should communicate fun and health using our Brightly Our Finest logo, bar code and nutritional data.

I will supply barcode.
Updates

Very disappointed writhe the designs I received.

Target Market(s)

Kids and Moms in the US Health and Wellness Niche

Industry/Entity Type

Health And Wellness

Font styles to use
Sans Serif

Colors

Designer to choose colors to be used in the design.

Requirements
Must have
• Brightly Our Finest LOGO, MoonRocket Drink Mix for Kids, 100% of the RDA for Fruits, Veggies and Protein, Organic, Non-GMO, USA Grown and Produced.

```html
<!DOCTYPE html>
<html lang="en">
<head>
<meta charset="utf-8">
<title>Moonrocket Meals for Kids – Label</title>
<link rel="stylesheet" href="https://fonts.googleapis.com/css2?family=Dancing+Script:wght@700&family=Lora:ital,wght@0,600;1,700&display=swap">
<style>
  :root {
    --canvas: #ffffff;
    --maroon: #8e1b22;
    --maroon-dark: #6e1218;
    --ribbon-red: #b3222b;
    --orange-light: #fbb417;
    --orange: #f58a1f;
    --orange-deep: #ef6f1f;
    --fruit-yellow: #f4b73a;
    --fruit-orange: #ef7d22;
    --fruit-red: #c9232e;
    --leaf-green: #4f8a3a;
    --badge-olive: #7a8a2a;
    --badge-blue: #2d6db5;
    --white: #ffffff;
  }
  html, body {
    margin: 0;
    width: 1200px;
    height: 1200px;
    overflow: hidden;
    background: var(--canvas);
  }
  .label {
    position: absolute;
    left: 50px;
    top: 406px;
    width: 1100px;
    height: 388px;
    overflow: hidden;
    background: linear-gradient(100deg, var(--fruit-orange) 0%, var(--fruit-yellow) 25%, var(--fruit-red) 48%, #a9323a 75%, #d8434a 100%);
  }
  .label-shapes {
    position: absolute;
    inset: 0;
  }
  .tagline {
    position: absolute;
    left: 401px;
    top: 30px;
    width: 278px;
    height: 30px;
    background: var(--maroon);
    color: var(--white);
    font: 600 22px/30px "Lora", serif;
    text-align: center;
    transform: rotate(-1deg);
  }
  .product-name {
    position: absolute;
    left: 380px;
    top: 78px;
    width: 380px;
    margin: 0;
    color: var(--white);
    font: 700 46px/50px "Dancing Script", cursive;
    text-align: center;
    transform: rotate(-8deg);
  }
  .origin {
    position: absolute;
    left: 820px;
    top: 22px;
    width: 260px;
    margin: 0;
    color: var(--maroon);
    font: 600 36px/54px "Lora", serif;
    text-align: center;
    -webkit-text-stroke: 1px var(--white);
  }
  .organic-seal {
    position: absolute;
    left: 892px;
    top: 128px;
    width: 132px;
    height: 132px;
    border-radius: 50%;
    background: var(--badge-olive);
    opacity: 0.85;
  }
  .rda-claim {
    position: absolute;
    left: 16px;
    top: 320px;
    margin: 0;
    color: var(--maroon);
    font: italic 700 31px/44px "Lora", serif;
  }
  .brand-box {
    position: absolute;
    left: 682px;
    top: 314px;
    width: 206px;
    height: 68px;
    background: var(--white);
    display: flex;
    align-items: center;
    justify-content: center;
    gap: 6px;
  }
  .brand-mark {
    width: 10px;
    height: 10px;
    border-radius: 50%;
    background: var(--leaf-green);
  }
  .brand-name {
    color: var(--leaf-green);
    font: 600 15px/1 "Lora", serif;
    letter-spacing: 0.5px;
    text-transform: uppercase;
  }
  .certification-badge {
    position: absolute;
    left: 901px;
    top: 306px;
    width: 167px;
    height: 76px;
    background: var(--badge-blue);
    border: 3px solid var(--white);
    box-sizing: border-box;
  }
</style>
</head>
<body>
  <section class="label">
    <svg class="label-shapes" width="1100" height="388" viewBox="0 0 1100 388" role="img" aria-label="Photograph of fresh oranges, lemons, tomatoes, red grapes and apples behind orange label panels">
      <defs>
        <linearGradient id="panelTop" x1="0" y1="0" x2="1" y2="0">
          <stop offset="0" stop-color="var(--orange-light)"/>
          <stop offset="1" stop-color="var(--orange-deep)"/>
        </linearGradient>
        <linearGradient id="panelBottom" x1="0" y1="0" x2="1" y2="0">
          <stop offset="0" stop-color="var(--orange-light)"/>
          <stop offset="0.8" stop-color="var(--orange)"/>
          <stop offset="1" stop-color="var(--orange)" stop-opacity="0"/>
        </linearGradient>
        <linearGradient id="ribbonFill" x1="0" y1="0" x2="1" y2="0">
          <stop offset="0" stop-color="var(--maroon-dark)"/>
          <stop offset="0.5" stop-color="var(--ribbon-red)"/>
          <stop offset="1" stop-color="var(--maroon)"/>
        </linearGradient>
      </defs>
      <path class="panel-top" d="M108,0 L1100,0 L1100,292 C930,286 720,276 600,256 L470,215 C380,170 310,110 108,0 Z" fill="url(#panelTop)"/>
      <path class="panel-bottom" d="M0,308 C140,284 360,268 580,292 L580,388 L0,388 Z" fill="url(#panelBottom)"/>
      <path class="ribbon" d="M330,110 C450,90 560,90 650,60 C700,44 730,30 748,16 C752,70 748,110 740,140 C690,160 620,172 560,180 C480,192 420,196 365,210 C380,180 372,140 330,110 Z" fill="url(#ribbonFill)" stroke="var(--white)" stroke-width="4"/>
    </svg>

    <div class="tagline">Veggies And Protein</div>
    <h1 class="product-name">Moonrocket Meals<br>For kids</h1>

    <p class="origin">Usa grown<br>And produced</p>
    <div class="organic-seal" role="img" aria-label="Organic natural product seal"></div>

    <p class="rda-claim">100% of the RDA for Fruits</p>

    <div class="brand-box">
      <span class="brand-mark"></span>
      <span class="brand-name">Brightly Our Finest</span>
    </div>
    <div class="certification-badge" role="img" aria-label="Non-GMO certification badge"></div>
  </section>
</body>
</html>
```